HTML Email Template

Hi,
I am looking to create a professional standardised email template. This is a basic html single page design, with my company details, logo and corporate colours etc, preferrably in a format suitable to email. Think a Outlook signature, but with a border around the email.
I will upload some basic samples, which will help to form the base of the design.

I just uploadedsome more files - 3 of them are logos (2 logos are the same, but I uploaded 2 sizes, please use whch is best)
I also uploaded another example (bad imaging I know) but the content of the page and the structure is what I want included also.
Thanks everyoine - Merry Christmas!

• must be editable, so I can edit the content of the emails.

```html
<!DOCTYPE html>
<html lang="en">
<head>
<meta charset="utf-8">
<title>Help Desk New Service Ticket Notification</title>
<link rel="stylesheet" href="https://fonts.googleapis.com/css2?family=Arimo:wght@400;700&family=Noto+Serif&family=Open+Sans:wght@400;600&display=swap">
<style>
  :root {
    --page-bg: #ffffff;
    --frame: #c9c9c9;
    --header-deep: #0d2f7a;
    --header-mid: #1f5fc4;
    --header-light: #6fa8ec;
    --band-green: #8dc26a;
    --band-green-dark: #78b257;
    --title-blue: #3256c8;
    --link-blue: #1d43b8;
    --text: #1a1a1a;
    --muted: #333333;
    --row-a: #e9eaee;
    --row-b: #f1f2f6;
    --rule: #cfcfcf;
    --badge-blue: #1e8fe0;
    --badge-navy: #1d3f8f;
    --icon-blue: #3a66b8;
    --icon-orange: #f08a22;
  }
  * { box-sizing: border-box; margin: 0; padding: 0; }
  html, body {
    width: 1137px; height: 1200px; overflow: hidden;
    background: var(--page-bg);
    font-family: "Arimo", Arial, sans-serif;
    color: var(--text);
  }
  .email {
    position: absolute; left: 145px; top: 0;
    width: 850px; height: 1150px;
    border: 1px solid var(--frame); border-top: none;
    background: var(--page-bg);
  }
  .header { position: absolute; left: 0; top: 0; width: 848px; height: 243px; overflow: hidden; }
  .header-sky {
    position: absolute; left: 0; top: 0; width: 100%; height: 154px;
    background: linear-gradient(100deg, var(--header-deep) 0%, var(--header-mid) 55%, var(--header-light) 100%);
  }
  .header-band {
    position: absolute; left: 0; top: 154px; width: 100%; height: 89px;
    background: linear-gradient(180deg, var(--band-green) 0%, var(--band-green-dark) 100%);
  }
  .header-visual {
    position: absolute; left: 313px; top: 0; width: 535px; height: 243px;
    background: radial-gradient(ellipse at 65% 40%, #cfdcea 0%, #8fb0d6 35%, rgba(60,110,190,0.6) 70%, rgba(60,110,190,0) 100%);
  }
  .brand { position: absolute; left: 25px; top: 48px; }
  .brand-name { font-family: "Open Sans", sans-serif; font-weight: 400; font-size: 44px; color: #ffffff; letter-spacing: 1px; line-height: 1; }
  .brand-tagline { font-family: "Open Sans", sans-serif; font-size: 12px; color: #ffffff; margin: 6px 0 0 98px; }
  .band-text {
    position: absolute; left: 20px; top: 160px;
    font-family: "Open Sans", sans-serif; font-size: 23px; line-height: 31px; color: #ffffff;
  }
  .social { position: absolute; left: 691px; top: 8px; display: flex; gap: 6px; }
  .social span { width: 31px; height: 31px; border-radius: 5px; background: var(--icon-blue); }
  .social span.feed { background: var(--icon-orange); }

  .title {
    position: absolute; left: 52px; top: 280px;
    font-family: "Noto Serif", serif; font-size: 28px; font-weight: 400;
    color: var(--title-blue); letter-spacing: 0.5px;
  }
  .message { position: absolute; left: 61px; top: 336px; width: 760px; font-size: 15px; line-height: 29px; }
  .greeting { font-size: 17px; font-weight: 700; margin-bottom: 12px; }
  .message ul { margin: 0 0 10px 23px; }
  .message li { padding-left: 0; }
  .signoff { margin-top: 2px; line-height: 26px; }
  .signoff a { color: var(--link-blue); font-weight: 700; text-decoration: none; }

  .detail-heading { position: absolute; left: 63px; top: 731px; font-size: 17px; font-weight: 700; color: var(--muted); }
  .ticket {
    position: absolute; left: 203px; top: 766px; width: 463px;
    border-collapse: collapse; font-size: 15px;
  }
  .ticket th, .ticket td { height: 42px; padding: 0 16px; text-align: left; border-bottom: 1px solid #fff; }
  .ticket th { width: 161px; font-weight: 700; border-right: 1px solid #fff; padding-left: 21px; }
  .ticket tr:nth-child(odd) { background: var(--row-a); }
  .ticket tr:nth-child(even) { background: var(--row-b); }

  .rule { position: absolute; left: 38px; top: 953px; width: 764px; border: none; border-top: 1px solid var(--rule); }
  .footer-note { position: absolute; left: 35px; top: 975px; font-size: 13px; line-height: 21px; color: var(--muted); }
  .copyright { position: absolute; left: 35px; top: 1078px; font-size: 13px; color: var(--muted); }
  .badge { position: absolute; top: 1061px; height: 50px; }
  .badge.specialist { left: 620px; width: 104px; border-radius: 4px; background: linear-gradient(180deg, #3fb0f2, var(--badge-blue)); }
  .badge.partner { left: 736px; width: 76px; border: 2px solid var(--badge-navy); background: linear-gradient(180deg, #ffffff 0 62%, var(--badge-navy) 62%); }
</style>
</head>
<body>
  <div class="email">
    <header class="header">
      <div class="header-sky"></div>
      <div class="header-band"></div>
      <div class="header-visual" role="img" aria-label="Photo of smiling IT support staff beside a row of servers"></div>
      <div class="brand">
        <div class="brand-name">Novaline IT</div>
        <div class="brand-tagline">your IT partner</div>
      </div>
      <div class="band-text">Tech Support, Business<br>Technology and Cloud Solutions</div>
      <div class="social" aria-label="Social links">
        <span></span><span></span><span></span><span class="feed"></span>
      </div>
    </header>

    <h1 class="title">HELP DESK NEW SERVICE TICKET NOTIFICATION</h1>

    <div class="message">
      <p class="greeting">Dear [contactfirstname]:</p>
      <p>We have received your email and ticket number <b>[srnumber],</b> related to "<b>[srsummary]</b>" has been created automatically.&nbsp; A technician will be working to address your issue shortly.</p>
      <p>Please reference the details listed below for more information.</p>
      <ul>
        <li>Error message &amp; user. Detailed error message with the issue and the name of the user.</li>
        <li>More details. Details of what the user was doing at the time</li>
        <li>Screen shots. Screen shots of your screen and/or error message.</li>
        <li>Screen name. Name of the screen and tab where the issue occurred</li>
      </ul>
      <p class="signoff">Thank you,<br>MY COMPANY SUPPORT<br><a href="mailto:support@novaline.example">support@novaline.example</a><br><a href="#">www.novaline.example</a></p>
    </div>

    <h2 class="detail-heading">SERVICE TICKET DETAIL</h2>
    <table class="ticket">
      <tr><th>Ticket Number:</th><td>[srnumber]</td></tr>
      <tr><th>Ticket Status:</th><td>[srstatus]</td></tr>
      <tr><th>Ticket Summary:</th><td>[srsummary]</td></tr>
      <tr><th>Ticket Detail:</th><td>[srdetail]</td></tr>
    </table>

    <hr class="rule">
    <p class="footer-note">THIS NOTIFICATION WAS CREATED BY NOVALINE IT SERVICES LTD HELP DESK SUPPORT TEAM<br>If you have any questions or wish to update information related to this ticket<br>simply reply to this email or call the help desk directly at 09-555-0142</p>
    <p class="copyright">Copyright © 2012 Novaline IT. All Rights Reserved.</p>
    <div class="badge specialist" aria-hidden="true"></div>
    <div class="badge partner" aria-hidden="true"></div>
  </div>
</body>
</html>
```